A WEBSITE FOR A JEWELLERY RETAIL STORE WITH A SHOPPING CART, AND ABILITY TO ORDER ONLINE.

I require a website with a shopping cart.

We sell MAINLY diamond jewellery (such as rings etc). I need it to be simple to change prices with only a few buttons, as the price fluctuates due to the US Dollar.

We are a diamond wholesaler, selling directly to the public, so we guarantee the lowest prices in Australia.

There is also a link to current inventory that will need to be uploaded to the site.

This could be an ongoing job, where you will be paid weekly to maintain and update the website if you wish.

Target Market(s)

People getting engaged, and wanting to buy a diamond ring.

Number of Pages Required

5+ page

Colors

Designer to choose colors to be used in the design.

Requirements
Must have
• elegant.
• modern.
• professional.
• SHOPPING CART.
• ABILITY TO SEARCH FOR LOOSE DIAMONDS (LINK THAT NEEDS TO BE EMBEDDED WILL BE SENT WHICH SHOWS CURRENT STOCK).
• ENGAGEMENT RINGS
• WEDDING RINGS
• DIAMOND EARRINGS
• DIAMOND PENDANTS
• LOOSE DIAMONDS.
• SALE ITEMS.
• OTHER JEWELLERY.
• EDUCATION
• WISH LIST
• CART.
Nice to have
• a good place to look for inspiration on pages is https://www.lumenvael.example.
• YOU MAY VISIT OUR FACEBOOK PAGE AT.
• HTTP://WWW.SOCIALPAGE.EXAMPLE/QUILLSTONEJEWELLERS
Should not have
• We don't want it too busy.

```html
<!DOCTYPE html>
<html lang="en">
<head>
<meta charset="utf-8">
<title>Quillstone Jewellers</title>
<link href="https://fonts.googleapis.com/css2?family=Cinzel:wght@400;600;700&family=Lato:wght@400;700&display=swap" rel="stylesheet">
<style>
:root{
  --ink:#222222;
  --topbar:#2a2a2a;
  --gold:#dcbf2c;
  --gold-text:#e0b52a;
  --beige:#eee1c6;
  --panel:#e9e9e9;
  --line:#dcdcdc;
  --muted:#6b6b6b;
  --footer:#262626;
  --footer-text:#9a9a9a;
  --white:#ffffff;
}
*{box-sizing:border-box;margin:0;padding:0}
html,body{width:1200px;height:3209px;overflow:hidden}
body{position:relative;background:var(--beige);font-family:'Lato',sans-serif;color:var(--ink)}
.serif{font-family:'Cinzel',serif}
.abs{position:absolute}

.topbar{left:0;top:0;width:1200px;height:40px;background:var(--topbar);font-family:'Cinzel',serif;font-size:11px;letter-spacing:.5px}
.topbar .call{left:172px;top:13px;color:var(--gold-text)}
.topbar .links{right:172px;top:13px;color:#d8d8d8;display:flex;gap:26px}
.topbar .links span::before{content:"";display:inline-block;width:8px;height:8px;border:1px solid var(--gold-text);border-radius:2px;margin-right:6px;vertical-align:-1px}

.header{left:0;top:40px;width:1200px;height:97px;background:var(--white)}
.brand{left:175px;top:24px;display:flex;align-items:center;gap:10px;font-family:'Cinzel',serif;font-weight:600;font-size:22px;color:var(--ink);letter-spacing:1px;line-height:1.05}
.brand .mark{width:34px;height:34px;background:var(--ink)}
.search{left:495px;top:35px;width:330px;height:36px;border:1px solid #cfcfcf;display:flex}
.search span{flex:1;font-size:12px;color:#8a8a8a;padding:11px 10px}
.search b{width:38px;background:var(--topbar);display:flex;align-items:center;justify-content:center}
.cart{left:865px;top:34px;display:flex;gap:12px;align-items:center;font-family:'Cinzel',serif;font-size:12px;line-height:1.5;letter-spacing:.5px}

.nav{left:0;top:137px;width:1200px;height:62px;background:var(--gold);display:flex;justify-content:center;gap:40px;align-items:center;font-family:'Cinzel',serif;font-size:16px;letter-spacing:1px;color:var(--ink)}

.hero{left:0;top:199px;width:1200px;height:582px;background:linear-gradient(90deg,#6b6b6b 0%,#8d8d8d 45%,#a8a8a8 60%,#5c5c5c 100%)}
.hero h1{left:172px;top:122px;font-family:'Cinzel',serif;font-weight:400;font-size:31px;line-height:37px;color:#fff;letter-spacing:.5px}
.hero p{left:172px;top:215px;font-family:'Cinzel',serif;font-size:14px;color:#fff;letter-spacing:.5px}
.btn{display:inline-block;font-family:'Cinzel',serif;font-size:13px;padding:12px 15px;letter-spacing:.5px}
.hero .b1{left:173px;top:253px;background:var(--gold);color:var(--ink)}
.hero .b2{left:351px;top:253px;background:var(--topbar);color:#fff}
.hero .arrow{top:274px}

.sheet{left:173px;top:686px;width:854px;height:2174px;background:var(--white)}
.band{left:173px;width:854px;background:var(--panel)}

.cat{top:721px;width:188px;height:252px;border:1px solid var(--line);background:#fff;text-align:center}
.cat h3{font-family:'Cinzel',serif;font-weight:400;font-size:13px;margin-top:25px;letter-spacing:.3px}
.cat .ph{width:150px;height:120px;margin:22px auto 0}
.cat .shop{position:absolute;left:0;right:0;bottom:18px;font-family:'Cinzel',serif;font-size:10px;text-decoration:underline}

.sec-title{left:173px;width:854px;text-align:center;font-family:'Cinzel',serif;font-weight:600;font-size:26px;letter-spacing:.5px}
.lede{left:173px;width:854px;text-align:center;font-size:13px;line-height:20px}
.shape{top:1191px;width:96px;height:100px;background:#fff;border:1px solid var(--line);border-radius:6px;display:flex;align-items:center;justify-content:center}
.shape-label{top:1296px;width:96px;text-align:center;font-family:'Cinzel',serif;font-size:12px}

.prod{width:192px;background:#fff;border:1px solid var(--line);text-align:center}
.prod .ph{width:160px;height:110px;margin:22px auto 0}
.prod .price{font-family:'Cinzel',serif;font-size:19px;margin-top:22px}
.prod p{font-size:13px;line-height:18px;margin-top:12px;color:#333}
.prod .buy{display:inline-block;background:var(--topbar);color:#fff;font-family:'Cinzel',serif;font-size:12px;padding:7px 18px;margin-top:14px;letter-spacing:.5px}

.feature{left:606px;top:1931px;width:401px;height:309px;background:radial-gradient(circle at 55% 60%,#8a8a8a 0%,#3a3a3a 45%,#111 80%)}
.feature h4{position:absolute;left:35px;top:26px;font-family:'Cinzel',serif;font-weight:400;font-size:13px;line-height:18px;color:#fff}
.feature .coll{position:absolute;right:20px;top:24px;background:#3a3a3a;color:#fff;font-family:'Cinzel',serif;font-size:12px;padding:7px 12px}

.edu{left:193px;top:2363px;width:812px;height:221px;border:1px solid var(--line);background:#fff}
.edu h2{position:absolute;left:46px;top:28px;font-family:'Cinzel',serif;font-weight:600;font-size:27px}
.edu p{position:absolute;left:46px;top:73px;width:440px;font-size:12px;line-height:19px}
.edu .topics{position:absolute;left:50px;top:130px;display:grid;grid-template-columns:186px 186px;row-gap:22px;font-family:'Cinzel',serif;font-size:12px}
.edu .gems{position:absolute;right:0;top:10px;width:360px;height:200px;background:radial-gradient(ellipse at center,#e4e4e4 0%,#f6f6f6 55%,#fff 80%)}

.photo{top:2640px;width:156px;height:160px}

.footer{left:0;top:2800px;width:1200px;height:409px;background:var(--footer)}
.fbrand{left:173px;top:2920px;display:flex;align-items:center;gap:10px;font-family:'Cinzel',serif;font-weight:600;font-size:19px;color:#fff;letter-spacing:1px;line-height:1.05}
.fbrand .mark{width:30px;height:30px;background:#fff}
.contact{left:173px;font-size:11px;color:var(--footer-text);display:flex;gap:12px;align-items:center;line-height:16px}
.contact i{width:22px;height:22px;border:1px solid #777;border-radius:50%;display:flex;align-items:center;justify-content:center;flex:none}
.fcol{top:2912px;font-size:11px;color:var(--footer-text);line-height:19px}
.fcol h5{font-size:15px;color:#fff;font-weight:700;margin-bottom:8px}
.fcol h5::after{content:"";display:block;width:22px;height:3px;background:var(--gold);margin-top:10px;margin-bottom:12px}
.frule{left:173px;top:3140px;width:854px;height:1px;background:#3e3e3e}
.socials{left:173px;top:3163px;display:flex;gap:8px}
.socials span{width:26px;height:26px;border-radius:50%}
.legal{right:173px;top:3170px;font-size:11px;color:var(--footer-text);display:flex;gap:14px}
</style>
</head>
<body>

<div class="abs topbar">
  <div class="abs call">&#9990; Call us on 00000 000 000</div>
  <div class="abs links"><span>My Account</span><span>Checkout</span><span>Wish List</span></div>
</div>

<header class="abs header">
  <div class="abs brand"><span class="mark"></span><span>QUILLSTONE<br>JEWELLERS</span></div>
  <div class="abs search"><span>Search Here</span><b><svg width="12" height="12" viewBox="0 0 12 12"><circle cx="5" cy="5" r="3.6" fill="none" stroke="#fff" stroke-width="1.5"/><line x1="7.7" y1="7.7" x2="11" y2="11" stroke="#fff" stroke-width="1.5"/></svg></b></div>
  <div class="abs cart">
    <svg width="30" height="26" viewBox="0 0 30 26"><rect x="3" y="8" width="18" height="16" fill="none" stroke="#dcbf2c" stroke-width="2"/><path d="M8 8V4a4 4 0 0 1 8 0v4" fill="none" stroke="#dcbf2c" stroke-width="2"/><rect x="17" y="13" width="11" height="11" fill="#dcbf2c"/></svg>
    <span>Shopping Cart<br>(0 items)</span>
  </div>
</header>

<nav class="abs nav"><span>DIAMONDS</span><span>ENGAGEMENT RINGS</span><span>WEDDING</span><span>JEWELRY</span><span>EDUCATION</span><span>ON SALE</span></nav>

<section class="abs hero" role="img" aria-label="Black and white photo of a woman wearing a diamond necklace and earrings">
  <h1 class="abs">YOU DESIGN IT WE<br>BUILD ITSHE SAYS YES</h1>
  <p class="abs">A SMARTER WAY TO BUY ENGAGEMENT RINGS</p>
  <span class="abs btn b1">ENGAGEMENT RINGS</span>
  <span class="abs btn b2">WEDDING RINGS</span>
  <svg class="abs arrow" style="left:30px" width="16" height="30" viewBox="0 0 16 30"><path d="M14 2L2 15l12 13" fill="none" stroke="#fff" stroke-width="2"/></svg>
  <svg class="abs arrow" style="left:1156px" width="16" height="30" viewBox="0 0 16 30"><path d="M2 2l12 13L2 28" fill="none" stroke="#fff" stroke-width="2"/></svg>
</section>

<div class="abs sheet"></div>

<div class="abs cat" style="left:193px"><h3>ENGAGEMENT RINGS</h3><div class="ph" role="img" aria-label="Heart cut diamond engagement ring" style="background:radial-gradient(ellipse,#d9d9d9,#fff 70%)"></div><span class="shop">SHOP NOW</span></div>
<div class="abs cat" style="left:402px"><h3>WEDDING RINGS</h3><div class="ph" role="img" aria-label="Diamond wedding ring" style="background:radial-gradient(ellipse,#d4d4d4,#fff 70%)"></div><span class="shop">SHOP NOW</span></div>
<div class="abs cat" style="left:610px"><h3>DIAMOND EARRINGS</h3><div class="ph" role="img" aria-label="Pair of diamond stud earrings" style="background:radial-gradient(ellipse,#d6d6d6,#fff 70%)"></div><span class="shop">SHOP NOW</span></div>
<div class="abs cat" style="left:817px"><h3>DIAMOND PENDANTS</h3><div class="ph" role="img" aria-label="Diamond halo pendant on a chain" style="background:radial-gradient(ellipse,#d6d6d6,#fff 70%)"></div><span class="shop">SHOP NOW</span></div>

<div class="abs band" style="top:1020px;height:355px"></div>
<h2 class="abs sec-title" style="top:1050px">LOOSE DIAMONDS</h2>
<p class="abs lede" style="top:1098px">Lorem ipsum dolor sit amet, consectetur adipiscing elit, sed do eiusmod tempidunt<br>et dolore magna aliquim ad mLorem ipsum dolor sit amet, consectetu</p>
<p class="abs lede" style="top:1152px;font-size:15px;text-decoration:underline">Search Loose Diamonds</p>

<div class="abs shape" style="left:193px"><svg width="64" height="64" viewBox="0 0 64 64" fill="none" stroke="#444" stroke-width="1.5"><circle cx="32" cy="32" r="28"/><polygon points="32,14 45,19 50,32 45,45 32,50 19,45 14,32 19,19"/></svg></div>
<div class="abs shape" style="left:296px"><svg width="64" height="64" viewBox="0 0 64 64" fill="none" stroke="#444" stroke-width="1.5"><rect x="6" y="6" width="52" height="52"/><path d="M6 6l52 52M58 6L6 58M20 20h24v24H20z"/></svg></div>
<div class="abs shape" style="left:398px"><svg width="64" height="64" viewBox="0 0 64 64" fill="none" stroke="#444" stroke-width="1.5"><path d="M32 2C44 18 44 46 32 62C20 46 20 18 32 2z"/><path d="M32 14C38 24 38 40 32 50C26 40 26 24 32 14z"/></svg></div>
<div class="abs shape" style="left:501px"><svg width="64" height="64" viewBox="0 0 64 64" fill="none" stroke="#444" stroke-width="1.5"><polygon points="20,4 44,4 50,10 50,54 44,60 20,60 14,54 14,10"/><rect x="22" y="14" width="20" height="36"/></svg></div>
<div class="abs shape" style="left:604px"><svg width="64" height="64" viewBox="0 0 64 64" fill="none" stroke="#444" stroke-width="1.5"><path d="M32 4C44 20 50 34 50 44a18 18 0 0 1-36 0c0-10 6-24 18-40z"/><path d="M32 20C38 30 40 38 40 44a8 8 0 0 1-16 0c0-6 2-14 8-24z"/></svg></div>
<div class="abs shape" style="left:707px"><svg width="64" height="64" viewBox="0 0 64 64" fill="none" stroke="#444" stroke-width="1.5"><ellipse cx="32" cy="32" rx="19" ry="28"/><ellipse cx="32" cy="32" rx="10" ry="16"/></svg></div>
<div class="abs shape" style="left:809px"><svg width="64" height="64" viewBox="0 0 64 64" fill="none" stroke="#444" stroke-width="1.5"><path d="M32 58L8 30C0 20 6 6 18 6c7 0 12 5 14 10C34 11 39 6 46 6c12 0 18 14 10 24z"/><path d="M32 44L20 30c-4-5-1-12 5-12 4 0 6 3 7 6 1-3 3-6 7-6 6 0 9 7 5 12z"/></svg></div>
<div class="abs shape" style="left:912px"><svg width="64" height="64" viewBox="0 0 64 64" fill="none" stroke="#444" stroke-width="1.5"><polygon points="18,4 46,4 60,18 60,46 46,60 18,60 4,46 4,18"/><polygon points="24,14 40,14 50,24 50,40 40,50 24,50 14,40 14,24"/></svg></div>

<span class="abs shape-label" style="left:193px">ROUND</span>
<span class="abs shape-label" style="left:296px">PRINCESS</span>
<span class="abs shape-label" style="left:398px">MARQUISE</span>
<span class="abs shape-label" style="left:501px">EMERALD</span>
<span class="abs shape-label" style="left:604px">PEAR</span>
<span class="abs shape-label" style="left:707px">OVAL</span>
<span class="abs shape-label" style="left:809px">HEART</span>
<span class="abs shape-label" style="left:912px">ASSCHER</span>
<svg class="abs" style="left:590px;top:1346px" width="20" height="6" viewBox="0 0 20 6"><circle cx="3" cy="3" r="2" fill="#666"/><circle cx="10" cy="3" r="2" fill="#222"/><circle cx="17" cy="3" r="2" fill="#666"/></svg>

<h2 class="abs sec-title" style="top:1408px">SALE ITEMS</h2>
<div class="abs prod" style="left:193px;top:1470px;height:310px"><div class="ph" role="img" aria-label="Diamond halo ring with pave band" style="background:radial-gradient(ellipse,#d2d2d2,#fff 70%)"></div><div class="price">$120,000</div><p>Lorem isum dolo sitm<br>consem isum do</p><span class="buy">BUY NOW</span></div>
<div class="abs prod" style="left:400px;top:1470px;height:310px"><div class="ph" role="img" aria-label="Solitaire diamond ring" style="background:radial-gradient(ellipse,#d2d2d2,#fff 70%)"></div><div class="price">$120,000</div><p>Lorem isum dolo sitm<br>consem isum do</p><span class="buy">BUY NOW</span></div>
<div class="abs prod" style="left:607px;top:1470px;height:310px"><div class="ph" role="img" aria-label="Yellow gold diamond halo ring" style="background:radial-gradient(ellipse,#ddd1ad,#fff 70%)"></div><div class="price">$120,000</div><p>Lorem isum dolo sitm<br>consem isum do</p><span class="buy">BUY NOW</span></div>
<div class="abs prod" style="left:814px;top:1470px;height:310px"><div class="ph" role="img" aria-label="Marquise diamond halo ring" style="background:radial-gradient(ellipse,#d2d2d2,#fff 70%)"></div><div class="price">$120,000</div><p>Lorem isum dolo sitm<br>consem isum do</p><span class="buy">BUY NOW</span></div>

<div class="abs band" style="top:1835px;height:475px"></div>
<h2 class="abs sec-title" style="top:1866px">OTHER JEWELLERY</h2>
<div class="abs prod" style="left:193px;top:1931px;height:309px"><div class="ph" role="img" aria-label="Diamond halo ring set" style="background:radial-gradient(ellipse,#d2d2d2,#fff 70%)"></div><div class="price">$120,000</div><p>Lorem isum dolo sitm<br>consem isum do</p><span class="buy">BUY NOW</span></div>
<div class="abs prod" style="left:400px;top:1931px;height:309px"><div class="ph" role="img" aria-label="Diamond stud earrings" style="background:radial-gradient(ellipse,#d2d2d2,#fff 70%)"></div><div class="price">$120,000</div><p>Lorem isum dolo sitm<br>consem isum do</p><span class="buy">BUY NOW</span></div>
<div class="abs feature" role="img" aria-label="Pear cut diamond ring on a dark background"><h4>LOREM ISUM DOLO SITM<br>CONSEM ISUM DO</h4><span class="coll">COLLECTIONS</span></div>

<div class="abs edu">
  <h2>EDUCATION</h2>
  <p>Lorem ipsum dolor sit amet, consectetur adipiscing elit, sed do eiusmod tempidunt et dolore magna aliquim ad mLorem ipsum dolor sit amet, consectetu</p>
  <div class="topics"><span>DIAMOND CUT</span><span>DIAMOND CLARITY</span><span>DIAMOND COLOR</span><span>CARAT WEIGHT</span></div>
  <div class="gems" role="img" aria-label="Loose diamonds of several cuts"></div>
</div>

<div class="abs photo" style="left:193px;background:linear-gradient(135deg,#b0141a,#e23a3a 60%,#5a0b0e)" role="img" aria-label="Hand with red nails holding a diamond ring"></div>
<div class="abs photo" style="left:358px;background:radial-gradient(circle,#d8d8d8,#6d6d6d 70%,#3b3b3b)" role="img" aria-label="Close view of a round brilliant diamond"></div>
<div class="abs photo" style="left:523px;background:linear-gradient(135deg,#efe9e2,#c9bfb6)" role="img" aria-label="Diamond band on white flowers"></div>
<div class="abs photo" style="left:688px;background:radial-gradient(circle,#6e7fc0,#1f2a6b 75%)" role="img" aria-label="Two diamonds on blue cloth"></div>
<div class="abs photo" style="left:851px;background:linear-gradient(135deg,#c99a8a,#8a5d52)" role="img" aria-label="Hand wearing a halo diamond ring"></div>

<footer class="abs footer"></footer>
<div class="abs sheet" style="top:2800px;height:60px"></div>

<div class="abs fbrand"><span class="mark"></span><span>QUILLSTONE<br>JEWELLERS</span></div>
<div class="abs contact" style="top:2989px"><i><svg width="10" height="12" viewBox="0 0 10 12"><path d="M5 11S1 6.5 1 4.2a4 4 0 0 1 8 0C9 6.5 5 11 5 11z" fill="none" stroke="#999"/></svg></i><span>Loremipsum loremh<br>lorem usll 767a loremtumy</span></div>
<div class="abs contact" style="top:3034px"><i><svg width="10" height="10" viewBox="0 0 10 10"><path d="M2 1l2 2-1 1.5c.8 1.5 1.7 2.4 3 3L7.5 6l2 2-1.5 1.5C4.5 9 1 5.5.5 2z" fill="#999"/></svg></i><span>Phone: (555) 010-2468</span></div>
<div class="abs contact" style="top:3065px"><i><svg width="12" height="9" viewBox="0 0 12 9"><rect x=".5" y=".5" width="11" height="8" fill="none" stroke="#999"/><path d="M.5 .5l5.5 4 5.5-4" fill="none" stroke="#999"/></svg></i><span>Email: info@quillstone.example</span></div>

<div class="abs fcol" style="left:402px"><h5>Products</h5>Lrem ipsum dolor<br>Sit amet,<br>Consectetur<br>Sadipscing elit<br>Sed do eiusm<br>Consectetur</div>
<div class="abs fcol" style="left:582px"><h5>Company</h5>About Us<br>Product Reviews<br>Privacy Policy<br>Terms &amp; Conditions<br>Site Map<br>Discount Policies<br>Advanced Search</div>
<div class="abs fcol" style="left:755px"><h5>My Account</h5>My Account<br>Order History<br>Wish List<br>Newsletter</div>
<div class="abs fcol" style="left:913px"><h5>Customer Care</h5>Order Info<br>Shipping / Tracking Info<br>Returns Info<br>Request Exchange<br>Guarantee</div>

<div class="abs frule"></div>
<div class="abs socials"><span style="background:#3b5a9a"></span><span style="background:#27a3e0"></span><span style="background:#3f77a6"></span><span style="background:#d2483a"></span><span style="background:#c82330"></span><span style="background:#cc2020"></span></div>
<div class="abs legal"><span>Copyright © 2018 All rights reserved</span><span>Privacy Policy</span><span>Terms &amp; Conditions</span></div>

</body>
</html>
```